Nimbo58.com.au Website and company image design

We are looking for an exceptional website designer / company to work with our new Australian Hosting Company

Nimbo58 is a new Cloud Hosting company launching in Australia that provides Scalable, On Demand computing resources to the Australian Market Place. Scalable, On Demand ocmputing is a nice way of saying fully scalable / redundant Virtual Private Server.

We require a full company image to be developed along with a Logo and Website. There is scope for ongoing development (preferred) for the successful candidate.

Website developement will require extensive jQuery ability (sliders for ordering etc (see: http://www.hostrix-example.com.au/virtual-dedicated-servers/253/zar_vps.html).

Please communicate directly with me to establish full website scope and request further documentation / content.

Target Market(s)

Website Designers, programmers, technicians and large companies

Industry/Entity Type

It Company

Requirements
Must have
• Slider ordering system such as http://www.hostrix-example.com.au/virtual-dedicated-servers/253/zar_vps.html

Nice to have
• CMS backend system
Should not have
• Should NOT be a monster template copy!!!

```html
<!DOCTYPE html>
<html lang="en">
<head>
<meta charset="utf-8">
<title>Nimbo58 – Fully Managed Servers</title>
<link rel="stylesheet" href="https://fonts.googleapis.com/css2?family=Ubuntu:wght@300;400;500;700&display=swap">
<style>
:root{
  --hero-bg:#343434;
  --hero-dark:#2a2a2a;
  --page-bg:#f2f2f0;
  --text-dark:#222;
  --text-body:#333;
  --white:#fff;
  --nav-bg:#ececec;
  --nav-text:#444;
  --accent-green:#6cb31e;
  --news-green:#8ed82a;
  --news-bg:#c3c3c3;
  --footer-bg:#333;
  --track:#262626;
}
*{box-sizing:border-box;margin:0;padding:0}
html,body{width:1200px;height:1200px;overflow:hidden}
body{background:var(--page-bg);font-family:"Ubuntu",sans-serif;color:var(--text-body);position:relative}
.abs{position:absolute}

/* hero */
.hero{left:0;top:0;width:1200px;height:612px;background:var(--hero-bg);border-bottom:3px solid #111}
.hero-photo{left:490px;top:145px;width:710px;height:464px;background:linear-gradient(90deg,rgba(52,52,52,1) 0%,rgba(70,74,76,.9) 30%,#5a5f61 60%,#4b4f50 100%)}
.brand{left:168px;top:100px;display:flex;align-items:center;gap:10px;color:var(--white);font-size:34px;font-weight:500}
.brand-dot{width:22px;height:22px;border-radius:50%;background:#2f8fd8}
.main-nav{left:490px;top:98px;width:600px;height:47px;background:linear-gradient(#f6f6f6,#dedede);border-radius:3px;display:flex;justify-content:space-between;align-items:center;padding:0 13px 0 19px;box-shadow:0 2px 4px rgba(0,0,0,.4)}
.main-nav a{font-size:12px;font-weight:500;color:var(--nav-text);text-decoration:none;letter-spacing:.3px}
.hero-title{left:82px;top:214px;font-size:34px;font-weight:700;color:var(--white)}
.hero-sub{left:118px;top:254px;font-size:12px;color:var(--white)}
.benefits{left:120px;top:300px;list-style:none}
.benefits li{display:flex;align-items:center;gap:11px;color:var(--white);font-size:17px;height:30px}
.read-more{left:135px;top:443px;width:218px;height:45px;background:var(--white);border-radius:4px;font-size:16px;font-weight:500;color:#555;display:flex;align-items:center;justify-content:center}

/* configurator */
.cfg-row{left:555px;width:480px;height:30px;display:flex;align-items:center;color:var(--white)}
.cfg-label{width:130px;font-size:19px;font-weight:300}
.cfg-label small{font-size:13px;color:#ccc}
.cfg-track{position:relative;width:230px;height:8px;border-radius:4px;background:var(--track);box-shadow:inset 0 1px 2px #000}
.cfg-knob{position:absolute;top:-5px;width:18px;height:18px;border-radius:50%;background:radial-gradient(circle at 40% 35%,#fff,#ccc)}
.cfg-value{margin-left:21px;font-size:19px;font-weight:300}
.cfg-value span{font-size:13px;color:#ccc;margin-left:6px}
.cost{left:684px;top:379px;color:var(--white);font-size:18px;font-weight:300}
.cost strong{font-weight:400;font-size:20px;margin-left:6px}
.next-step{left:885px;top:376px;width:103px;height:31px;background:var(--white);border-radius:2px;font-size:16px;color:#444;display:flex;align-items:center;justify-content:center}
.hero-blurb{left:546px;top:453px;width:490px;font-size:13.5px;line-height:17px;color:var(--white)}

/* features */
.features{left:110px;top:582px;width:980px;height:229px;display:flex}
.feature{height:100%;background:linear-gradient(90deg,#ececec,#fff);text-align:center;position:relative}
.feature-art{width:74px;height:62px;margin:20px auto 0;border-radius:8px}
.feature h3{font-size:15px;font-weight:400;color:var(--text-dark);margin-top:18px}
.feature p{font-size:11px;line-height:18.5px;color:var(--text-dark);width:270px;margin:10px auto 0}
.feature .more{display:inline-block;margin-top:7px;width:57px;height:20px;border:1px solid #9aa6b0;border-radius:3px;background:linear-gradient(#f3f6f8,#b9c6d1);font-size:11px;color:#445;line-height:18px}

/* welcome */
.welcome{left:140px;top:850px;width:628px}
.welcome h1{font-size:25px;font-weight:300;color:var(--text-dark)}
.welcome h2{font-size:17px;font-style:italic;font-weight:500;color:var(--accent-green);margin-top:17px}
.welcome p{font-size:13.5px;line-height:16px;text-align:justify;margin-top:18px;color:#444}
.news{left:800px;top:841px;width:290px;height:209px;background:var(--news-bg);border-radius:20px;padding:14px 20px}
.news h3{font-size:20px;font-weight:500;color:var(--news-green)}
.news-item{margin-top:9px;font-size:11.5px;line-height:16px;color:#111}
.news-item p{text-align:justify}
.news-item+.news-item{margin-top:10px}

/* footer */
.site-footer{left:110px;top:1079px;width:980px;height:51px;background:linear-gradient(#3a3a3a,#2c2c2c);border-radius:3px;display:flex;align-items:center;justify-content:space-between;padding:0 15px 0 16px;font-size:12px;font-weight:300;color:var(--white)}
.site-footer nav a{color:var(--white);text-decoration:none}
.site-footer nav i{font-style:normal;margin:0 7px}
</style>
</head>
<body>

<header class="hero abs">
  <div class="hero-photo abs" role="img" aria-label="Photo of a data centre aisle lined with server racks"></div>
  <div class="brand abs"><span class="brand-dot"></span>Nimbo58</div>
  <nav class="main-nav abs">
    <a href="#">DOMAINS</a><a href="#">WEB HOSTING</a><a href="#">CLOUD MACHINES</a><a href="#">WHY NIMBO58</a><a href="#">GET IN TOUCH</a>
  </nav>

  <h1 class="hero-title abs">Fully Managed Servers</h1>
  <p class="hero-sub abs">you focus on your business and we take care of rest.</p>
  <ul class="benefits abs">
    <li><svg width="14" height="14" viewBox="0 0 14 14"><circle cx="7" cy="7" r="7" fill="#e8eef4"/><path d="M3.8 7.2l2.2 2.2 4.2-4.4" stroke="#3a8fd0" stroke-width="1.8" fill="none"/></svg>Fibre Optice for High Performance</li>
    <li><svg width="14" height="14" viewBox="0 0 14 14"><circle cx="7" cy="7" r="7" fill="#e8eef4"/><path d="M3.8 7.2l2.2 2.2 4.2-4.4" stroke="#3a8fd0" stroke-width="1.8" fill="none"/></svg>Protected from Security Threats</li>
    <li><svg width="14" height="14" viewBox="0 0 14 14"><circle cx="7" cy="7" r="7" fill="#e8eef4"/><path d="M3.8 7.2l2.2 2.2 4.2-4.4" stroke="#3a8fd0" stroke-width="1.8" fill="none"/></svg>Secure in a local DataCenter</li>
  </ul>
  <div class="read-more abs">READ MORE ABOUT US</div>

  <div class="cfg-row abs" style="top:242px">
    <div class="cfg-label">vCPU <small>2.4Ghz</small></div>
    <div class="cfg-track"><span class="cfg-knob" style="left:58px"></span></div>
    <div class="cfg-value">3<span>Cores</span></div>
  </div>
  <div class="cfg-row abs" style="top:282px">
    <div class="cfg-label">Memory</div>
    <div class="cfg-track"><span class="cfg-knob" style="left:28px"></span></div>
    <div class="cfg-value">1<span>GB</span></div>
  </div>
  <div class="cfg-row abs" style="top:322px">
    <div class="cfg-label">Storage</div>
    <div class="cfg-track"><span class="cfg-knob" style="left:118px"></span></div>
    <div class="cfg-value">25<span>GB</span></div>
  </div>
  <div class="cost abs">Monthly Cost: <strong>$50.00</strong></div>
  <div class="next-step abs">Next Step</div>
  <p class="hero-blurb abs">Lorem Ipsum est simplement du faux texte employé dans la composition et la mise en page avant impression. Le Lorem Ipsum est le faux texte standard de l'imprimerie depuis les années 1500</p>
</header>

<section class="features abs">
  <article class="feature" style="width:334px">
    <div class="feature-art" style="background:linear-gradient(#7fd3e6,#2bb0cc);border-radius:30px 30px 12px 12px" role="img" aria-label="Illustration of a cloud with a bandage"></div>
    <h3>Self Healing Hardware</h3>
    <p>Le Lorem Ipsum est simplement du faux texte employé dans la composition et la mise en page avant impression.</p>
    <span class="more">More</span>
  </article>
  <article class="feature" style="width:324px">
    <div class="feature-art" style="width:86px;height:54px;margin-top:22px;border-radius:2px;background:linear-gradient(#6cc4f5,#3aa3ea)" role="img" aria-label="Blueprint illustration of a cloud with dimension arrows"></div>
    <h3 style="margin-top:24px">Highly Scalable</h3>
    <p>Le Lorem Ipsum est simplement du faux texte employé dans la composition et la mise en page avant impression.</p>
    <span class="more">More</span>
  </article>
  <article class="feature" style="width:322px">
    <div class="feature-art" style="width:72px;height:66px;margin-top:15px;border-radius:4px;background:linear-gradient(135deg,#d8d8d8,#6a6e72)" role="img" aria-label="Illustration of a hard drive with a globe"></div>
    <h3 style="margin-top:21px">Cloud Data Storage</h3>
    <p>Le Lorem Ipsum est simplement du faux texte employé dans la composition et la mise en page avant impression.</p>
    <span class="more">More</span>
  </article>
</section>

<section class="welcome abs">
  <h1>Welcome</h1>
  <h2>Plusieurs variations de Lorem Ipsum</h2>
  <p>Lorem Ipsum est simplement du faux texte employé dans la composition et la mise en page avant impression. Le Lorem Ipsum est le faux texte standard de l'imprimerie depuis les années 1500, quand un peintre anonyme assembla ensemble des morceaux de texte pour réaliser un livre spécimen de polices de texte. Il n'a pas fait que survivre cinq siècles, mais s'est aussi adapté à la bureautique informatique, sans que son contenu n'en soit modifié.</p>
</section>

<aside class="news abs">
  <h3>News Feed</h3>
  <div class="news-item"><div>3rd dec 2012</div><p>Lorem Ipsum est simplement du faux texte employé dans la composition et la mise en page avant impression.</p></div>
  <div class="news-item"><div>3rd dec 2012</div><p>Lorem Ipsum est simplement du faux texte employé dans la composition et la mise en page avant impression.</p></div>
</aside>

<footer class="site-footer abs">
  <nav><a href="#">Home</a><i>|</i><a href="#">About Us</a><i>|</i><a href="#">Our Services</a><i>|</i><a href="#">Our work</a><i>|</i><a href="#">Contact</a><i>|</i><a href="#">Terms and Conditions</a></nav>
  <span>© 2012 Brightfold Pty Ltd - ABN 42 318 905 264</span>
</footer>

</body>
</html>
```